Business Cards for a unique Russian patisserie

VORKA Russian Treats bakery intends to introduce Australian public to amazing Russian pastries and traditions of genuine Russian hospitality.
VORKA business model is a café, selling a mix of Russian, Eastern European and traditional pastries produced in-house.
VORKA’s ultimate goal is to create a superior eating experience and to become a destination eatery in Sydney.
I would like the business cards match our ambitious purpose, to be unique and bold. I want them to be sophisticated (as opposed to straightforward and tacky) and graphical. I would love if Russian national ornament (hohloma) elements to be used.
Dominating colours - red and black. For the styling guide please see our logo attached.
Target Market(s)
Business partners, suppliers, possible corporate clients
Industry/Entity Type
Bakery
Look and feel

```html
<!DOCTYPE html>
<html lang="en">
<head>
<meta charset="utf-8">
<title>VORKA Russian Treats – Business Cards</title>
<link href="https://fonts.googleapis.com/css2?family=Open+Sans:wght@400;700&display=swap" rel="stylesheet">
<style>
  :root{
    --backdrop:#e9e4dc;
    --cream:#f3f1e6;
    --chocolate:#3d2a22;
    --cherry:#dc1f2e;
    --cherry-dark:#b5121f;
    --ink:#4a3a33;
    --white:#ffffff;
  }
  *{box-sizing:border-box;margin:0;padding:0}
  html,body{width:1200px;height:1023px;overflow:hidden}
  body{
    background:var(--backdrop);
    font-family:'Open Sans',Arial,sans-serif;
    position:relative;
  }
  .card{
    position:absolute;
    top:200px;
    width:380px;
    height:620px;
    border-radius:4px;
    overflow:hidden;
    box-shadow:0 8px 24px rgba(0,0,0,.18);
  }
  /* Front card */
  .card--front{left:170px;background:var(--cream)}
  .drip-border{
    position:absolute;top:0;left:0;width:100%;height:120px;
    background:var(--chocolate);
    border-radius:0 0 40px 40px / 0 0 30px 30px;
  }
  .brand{
    position:absolute;top:170px;left:0;width:100%;
    display:flex;flex-direction:column;align-items:center;
  }
  .brand__dot{
    width:110px;height:110px;border-radius:50%;
    background:var(--cherry);margin-bottom:22px;
  }
  .brand__name{
    font-weight:700;color:var(--chocolate);
    font-size:64px;line-height:1;letter-spacing:2px;
  }
  .brand__tagline{
    font-weight:700;color:var(--chocolate);
    font-size:18px;margin-top:4px;letter-spacing:1px;
  }
  .contact{
    position:absolute;top:420px;left:0;width:100%;
    text-align:center;color:var(--ink);
  }
  .contact__name{font-weight:700;font-size:22px;letter-spacing:1px}
  .contact__role{font-size:13px;margin-bottom:18px}
  .contact__line{
    display:flex;flex-direction:column;align-items:center;
    font-size:15px;margin-bottom:8px;
  }
  .contact__icon{width:14px;height:14px;margin-bottom:3px}
  .web-strip{
    position:absolute;bottom:0;left:0;width:100%;height:44px;
    background:var(--cherry);color:var(--white);
    font-weight:700;font-size:15px;letter-spacing:2px;
    display:flex;align-items:center;justify-content:center;
  }
  /* Back card */
  .card--back{
    left:650px;background:var(--cherry);
    display:flex;flex-direction:column;align-items:center;justify-content:center;
  }
  .back__dot{
    width:260px;height:260px;border-radius:50%;
    background:var(--cream);margin-bottom:34px;
  }
  .back__name{
    font-weight:700;color:var(--cream);
    font-size:72px;line-height:1;letter-spacing:2px;
  }
  .back__tagline{
    font-weight:700;color:var(--cream);
    font-size:20px;margin-top:6px;letter-spacing:1px;
  }
</style>
</head>
<body>
  <section class="card card--front">
    <div class="drip-border" role="img" aria-label="Chocolate drip border"></div>
    <div class="brand">
      <div class="brand__dot"></div>
      <div class="brand__name">VORKA</div>
      <div class="brand__tagline">Russian Treats</div>
    </div>
    <div class="contact">
      <div class="contact__name">MARCO BELLINI</div>
      <div class="contact__role">Director</div>
      <div class="contact__line">
        <svg class="contact__icon" viewBox="0 0 14 14"><circle cx="7" cy="7" r="7" fill="#dc1f2e"/><rect x="4.5" y="3" width="5" height="8" rx="1" fill="none" stroke="#fff" stroke-width="1.2"/></svg>
        <span>0400 555 123</span>
      </div>
      <div class="contact__line">
        <svg class="contact__icon" viewBox="0 0 14 14"><circle cx="7" cy="7" r="7" fill="#dc1f2e"/><rect x="3.5" y="4.5" width="7" height="5" fill="none" stroke="#fff" stroke-width="1.1"/><path d="M3.5 4.5 L7 7.5 L10.5 4.5" fill="none" stroke="#fff" stroke-width="1.1"/></svg>
        <span>marco@vorka.com.au</span>
      </div>
    </div>
    <div class="web-strip">www.vorka.com.au</div>
  </section>

  <section class="card card--back">
    <div class="back__dot"></div>
    <div class="back__name">VORKA</div>
    <div class="back__tagline">Russian Treats</div>
  </section>
</body>
</html>
```